Paper Lantern Theory - Podcast Cover

Paper Lantern Theory is a weekly podcast that dispels some of the myths about conventional economic thinking and provides a new way of thinking about issues that are faced by the global economy. It's insightful, thought-provoking and, most importantly, fun. We are refreshing the look and sound of the podcast. I have attached a copy of the old amateur design (which I did!)

Target Market(s)

Male oriented, smart folk with an interest in politics and economics

Font styles to use
Sans Serif

Requirements
Must have
• Clearly visible title, even when reduced in size. Must be 3000 pixels by 3000 pixels.
Nice to have
• This podcast challenges the status quo. It should reflect that. Photos and names of the hosts. Actually, because th ephotos are so different, we'd be open to the idea of a caricature if you can do that within the price.

```html
<!DOCTYPE html>
<html lang="en">
<head>
<meta charset="utf-8">
<title>Paper Lantern Theory Podcast Cover</title>
<link rel="stylesheet" href="https://fonts.googleapis.com/css2?family=Archivo+Black&family=Caveat:wght@700&display=swap">
<style>
  :root {
    --bg: #000000;
    --red: #ed1c24;
    --white: #ffffff;
    --rule-red: #5a0a0d;
  }
  html, body {
    margin: 0;
    padding: 0;
    width: 1200px;
    height: 1200px;
    overflow: hidden;
    background: var(--bg);
  }
  .cover {
    display: block;
    width: 1200px;
    height: 1200px;
  }
  .display { font-family: "Archivo Black", "Arial Black", sans-serif; }
  .script { font-family: "Caveat", cursive; }
  .fill-red { fill: var(--red); }
  .fill-white { fill: var(--white); }
</style>
</head>
<body>
<svg class="cover" viewBox="0 0 1200 1200" xmlns="http://www.w3.org/2000/svg">
  <defs>
    <radialGradient id="backdrop-glow" cx="0.5" cy="0.35" r="0.6">
      <stop offset="0" stop-color="#9e1117" stop-opacity="0.75"/>
      <stop offset="0.6" stop-color="#4a0609" stop-opacity="0.45"/>
      <stop offset="1" stop-color="#000" stop-opacity="0"/>
    </radialGradient>
    <linearGradient id="host-left-fade" x1="0" y1="0" x2="0" y2="1">
      <stop offset="0" stop-color="#c9a58f"/>
      <stop offset="0.45" stop-color="#2f8fa8"/>
      <stop offset="0.9" stop-color="#1d5f72"/>
      <stop offset="1" stop-color="#000"/>
    </linearGradient>
    <linearGradient id="host-right-fade" x1="0" y1="0" x2="0" y2="1">
      <stop offset="0" stop-color="#b8a79a"/>
      <stop offset="0.45" stop-color="#e3e0da"/>
      <stop offset="0.9" stop-color="#cfccc6"/>
      <stop offset="1" stop-color="#000"/>
    </linearGradient>
  </defs>

  <rect width="1200" height="1200" fill="var(--bg)"/>

  <!-- decorative backdrop behind hosts -->
  <rect class="host-backdrop" role="img" aria-label="Decorative red chart backdrop suggesting rising growth"
        x="58" y="80" width="1063" height="400" fill="url(#backdrop-glow)"/>
  <g class="backdrop-rules" stroke="var(--rule-red)" stroke-width="1">
    <line x1="58" y1="298" x2="1121" y2="298"/>
    <line x1="58" y1="376" x2="1121" y2="376"/>
    <line x1="58" y1="455" x2="1121" y2="455"/>
  </g>

  <!-- host portraits -->
  <path class="host-photo host-left" role="img" aria-label="Portrait photo of host Neil Barrow, smiling, in a teal polo shirt"
        d="M75,528 L110,420 Q150,330 250,300 L268,170 Q280,80 345,80 Q415,80 428,170 L440,295 Q560,320 585,420 L609,528 Z"
        fill="url(#host-left-fade)"/>
  <path class="host-photo host-right" role="img" aria-label="Portrait photo of host Grant Vale, arms folded, in a white t-shirt"
        d="M680,528 L690,400 Q705,320 790,300 L817,130 Q825,70 885,68 Q950,70 960,130 L975,295 Q1045,320 1055,400 L1059,528 Z"
        fill="url(#host-right-fade)"/>

  <!-- host names -->
  <text class="display host-name" x="112" y="512" font-size="58" textLength="427" lengthAdjust="spacingAndGlyphs">
    <tspan class="fill-white">NEIL </tspan><tspan class="fill-red">BARROW</tspan>
  </text>
  <text class="script host-title fill-red" x="836" y="458" font-size="30">Prof</text>
  <text class="display host-name" x="653" y="517" font-size="58" textLength="420" lengthAdjust="spacingAndGlyphs">
    <tspan class="fill-white">GRANT </tspan><tspan class="fill-red">VALE</tspan>
  </text>

  <!-- title lockup -->
  <g class="title-rules" fill="var(--white)">
    <polygon points="92,677 472,675 472,679"/>
    <polygon points="739,675 1121,677 739,679"/>
    <polygon points="93,1061 360,1059 360,1063"/>
    <polygon points="854,1059 1121,1061 854,1063"/>
  </g>
  <text class="display title-kicker fill-white" x="605" y="702" font-size="86" text-anchor="middle">THE</text>
  <text class="display title-main fill-red" x="98" y="848" font-size="132" textLength="1029" lengthAdjust="spacingAndGlyphs">PAPER LANTERN</text>
  <text class="display title-main fill-red" x="612" y="990" font-size="148" text-anchor="middle">THEORY</text>
  <text class="display title-footer fill-white" x="610" y="1087" font-size="82" text-anchor="middle">PODCAST</text>
</svg>
</body>
</html>
```